Webdesign für Vermietung eines Ferienhauses auf der Insel Usedom
Zielgruppe
Vermietung eines Ferienhauses auf der Insel Usedom
ZG: Urlauber im gehobenem Preissegment, die Luxus schätzen und urlauben wollen
Aufgabenstellung
- IN ADOBE PHOTOSHOP
- Bilder können hier entnommen werden: https://www.quartiro-net.example/ob-link-ansicht-reserve/index.php?portal=48127&unit=39502/index.html
- gern können Sie auch Stock-Bilder verwenden
- Der Buchungskalender /die Verfügbarkeit der freien Zeiträume soll präsent im oberen Bereich der Seite stehen
- Lumivo-Bewertungsbutton
- Es gibt kein Logo - bitte den Namenszug 'KIEFERNVILLA*****HOLMSTEDE' nutzen

```html
<!DOCTYPE html>
<html lang="de">
<head>
<meta charset="utf-8">
<title>Kiefernvilla Holmstede – 5 Sterne Strandhaus</title>
<link href="https://fonts.googleapis.com/css2?family=DM+Sans:wght@400;500;700&family=DM+Serif+Display&display=swap" rel="stylesheet">
<style>
:root{
  --ink:#141414;
  --text:#4a4a4a;
  --gold:#e2b13c;
  --cream:#f8f6ef;
  --paper:#fcfcf9;
  --white:#ffffff;
  --line:#e6e3da;
  --black:#0e0e0e;
}
*{box-sizing:border-box;margin:0;padding:0}
html,body{width:1200px;height:3722px;overflow:hidden}
body{position:relative;background:var(--white);font-family:"DM Sans",Arial,sans-serif;color:var(--text)}
.abs{position:absolute}

/* header */
.site-header{position:absolute;left:0;top:0;width:1200px;height:97px;background:var(--white)}
.brand{position:absolute;left:0;top:0;width:282px;height:97px;background:var(--black);display:flex;align-items:center;justify-content:center}
.brand-name{font-family:"DM Sans",Arial,sans-serif;font-weight:500;font-size:17px;line-height:22px;color:var(--white);text-align:center}
.main-nav{position:absolute;left:337px;top:38px;display:flex;gap:34px;font-size:13px;color:#5a5a5a}
.main-nav .active{color:#c8962a;border-bottom:2px solid var(--gold);padding-bottom:8px}
.badge-shape{position:absolute;left:1034px;top:22px;width:116px;height:52px;border:2px solid #bdbdbd;border-radius:4px}

/* hero */
.hero-photo{position:absolute;left:0;top:97px;width:698px;height:481px;background:linear-gradient(120deg,#6e8a4a 0%,#a7a196 30%,#f2f1ee 55%,#e7e5e0 100%)}
.hero-panel{position:absolute;left:698px;top:97px;width:502px;height:481px;background:linear-gradient(160deg,#dcd6c6,#ece8df 50%,#d9d4c6)}
.hero-panel h2{position:absolute;left:109px;top:136px;font-size:19px;font-weight:500;color:var(--ink);letter-spacing:.5px}
.field{position:absolute;height:31px;background:#fbfaf6}
.field .ico{position:absolute;left:0;top:0;width:31px;height:31px;background:#f0e0b4;display:flex;align-items:center;justify-content:center}
.btn-gold{position:absolute;background:var(--gold);color:var(--ink);font-weight:500;display:flex;align-items:center;justify-content:center}
.or-line{position:absolute;left:109px;top:281px;width:285px;height:1px;background:#8a8678}
.or-line span{position:absolute;left:116px;top:-7px;background:#e4dfd3;padding:0 8px;font-size:10px;letter-spacing:3px;color:#555}
.review-text{position:absolute;left:109px;top:312px;font-size:13px;line-height:15px;color:var(--ink)}
.review-btn{position:absolute;left:288px;top:308px;width:104px;height:40px;background:var(--white);display:flex;align-items:center;justify-content:center;gap:6px;font-size:17px;font-weight:500;color:#3b6fd1}
.review-btn i{display:block;width:8px;height:8px;background:var(--gold)}

/* features */
.features{position:absolute;left:0;top:578px;width:1200px;height:125px;background:var(--cream)}
.feature{position:absolute;top:28px;width:160px;margin-left:-80px;text-align:center;font-size:11.5px;line-height:18px;color:#555}
.feature svg{display:block;margin:0 auto 8px}

/* sections */
.cream-bg{position:absolute;background:var(--cream)}
.paper-box{position:absolute;background:var(--paper)}
.eyebrow{position:absolute;font-size:11px;letter-spacing:1.8px;font-weight:500;color:#333;text-transform:uppercase;line-height:14px}
.eyebrow::before{content:"";position:absolute;left:-70px;top:6px;width:56px;height:1px;background:var(--gold)}
.heading{position:absolute;font-family:"DM Serif Display",Georgia,serif;font-weight:400;color:var(--ink);white-space:nowrap}
.heading-xl{font-size:47px;line-height:54px}
.heading-l{font-size:40px;line-height:46px}
.body-copy{position:absolute;font-size:15px;line-height:24px;color:var(--text)}
.photo{position:absolute}

/* faq */
.q{position:absolute;font-size:12px;font-weight:700;letter-spacing:1.8px;color:var(--ink)}
.divider{position:absolute;height:1px;background:#eeece6}

/* footer */
.site-footer{position:absolute;left:0;top:3446px;width:1200px;height:276px;background:var(--black);color:var(--white)}
.footer-brand{position:absolute;left:67px;top:72px;width:143px;text-align:center}
.footer-nav{position:absolute;right:68px;top:84px;display:flex;gap:22px;font-size:13px}
.footer-rule{position:absolute;left:518px;top:127px;width:614px;height:1px;background:#d8d8d8}
.footer-legal{position:absolute;right:68px;top:150px;display:flex;gap:24px;font-size:11px}
.footer-about{position:absolute;left:67px;top:154px;font-size:11px;line-height:22px}
</style>
</head>
<body>

<header class="site-header">
  <div class="brand">
    <div class="brand-name">KIEFERNVILLA<br>HOLMSTEDE</div>
  </div>
  <nav class="main-nav">
    <span class="active">Home</span><span>Das 5* Strandhaus</span><span>Verfügbarkeit</span><span>Die Räumlichkeiten</span><span>Lage</span><span>Kontakt</span>
  </nav>
  <div class="badge-shape" role="img" aria-label="Klassifizierungs-Siegel"></div>
</header>

<div class="hero-photo" role="img" aria-label="Weißes Reetdachhaus mit Holzterrasse und Gartenmöbeln"></div>
<section class="hero-panel" aria-label="Verfügbarkeit prüfen">
  <h2>VERFÜGBARKEIT PRÜFEN</h2>
  <div class="field" style="left:109px;top:175px;width:133px">
    <span class="ico"><svg width="11" height="11" viewBox="0 0 12 12" fill="none" stroke="#7a6a3a"><rect x="1" y="2" width="10" height="9"/><path d="M1 5h10M4 1v2M8 1v2"/></svg></span>
  </div>
  <div class="field" style="left:261px;top:175px;width:133px">
    <span class="ico"><svg width="11" height="11" viewBox="0 0 12 12" fill="none" stroke="#7a6a3a"><rect x="1" y="2" width="10" height="9"/><path d="M1 5h10M4 1v2M8 1v2"/></svg></span>
  </div>
  <div class="field" style="left:109px;top:223px;width:133px">
    <span class="ico"><svg width="12" height="11" viewBox="0 0 12 11" fill="none" stroke="#7a6a3a"><circle cx="4.5" cy="3.5" r="2"/><path d="M1 10c0-2 1.5-3.5 3.5-3.5S8 8 8 10M8.5 2a2 2 0 010 3.5M11 10c0-1.5-.8-2.7-2-3.2"/></svg></span>
  </div>
  <div class="btn-gold" style="left:261px;top:223px;width:133px;height:31px;font-size:14px">Jetzt Prüfen</div>
  <div class="or-line"><span>ODER</span></div>
  <div class="review-text">Sehen Sie, was andere<br>Gäste sagen</div>
  <div class="review-btn">Lumivo <i></i></div>
</section>

<section class="features">
  <div class="feature" style="left:158px">
    <svg width="26" height="22" viewBox="0 0 26 22" fill="#666"><path d="M13 1L1 11h4v10h6v-6h4v6h6V11h4z"/></svg>145 qm Wohnfläche<br>700qm Grundstück</div>
  <div class="feature" style="left:321px">
    <svg width="26" height="24" viewBox="0 0 26 24" fill="#666"><circle cx="7" cy="3" r="3"/><circle cx="19" cy="3" r="3"/><rect x="4" y="7" width="6" height="9" rx="1"/><path d="M16 7h6l2 9h-10z"/><rect x="5" y="16" width="4" height="8"/><rect x="17" y="16" width="4" height="8"/></svg>Platz für bis<br>zu 7 Personen</div>
  <div class="feature" style="left:480px">
    <svg width="26" height="22" viewBox="0 0 26 22" fill="#666"><path d="M3 9a10 7 0 0120 0z"/><rect x="12" y="8" width="2" height="11"/><rect x="2" y="19" width="22" height="2"/></svg>Nur 5 Gehminuten<br>zum Strand</div>
  <div class="feature" style="left:656px">
    <svg width="26" height="22" viewBox="0 0 26 22" fill="#666"><rect x="1" y="1" width="24" height="5"/><rect x="2" y="6" width="5" height="15"/><rect x="19" y="6" width="5" height="15"/><path d="M9 20c-1-4 3-5 4-10 2 4 5 6 4 10z"/></svg>Kamin für<br>gemütliche Abende</div>
  <div class="feature" style="left:850px">
    <svg width="26" height="22" viewBox="0 0 26 22" fill="none" stroke="#666" stroke-width="2"><path d="M8 14V3a2 2 0 014 0M16 14V3a2 2 0 014 0M8 8h8M1 17c3 0 3-2 6-2s3 2 6 2 3-2 6-2 3 2 6 2M1 21c3 0 3-2 6-2s3 2 6 2 3-2 6-2 3 2 6 2"/></svg>Eigene Sauna und<br>ganzjährlicher Whirlpool</div>
  <div class="feature" style="left:1057px">
    <svg width="26" height="22" viewBox="0 0 26 22" fill="#666"><rect x="1" y="2" width="4" height="4"/><rect x="8" y="3" width="17" height="2"/><rect x="1" y="9" width="4" height="4"/><rect x="8" y="10" width="17" height="2"/><rect x="1" y="16" width="4" height="4"/><rect x="8" y="17" width="17" height="2"/></svg>Entdecken Sie<br>alle Vorteile -&gt;</div>
</section>

<!-- welcome section -->
<div class="cream-bg" style="left:0;top:703px;width:1200px;height:672px"></div>
<div class="paper-box" style="left:29px;top:703px;width:1105px;height:642px"></div>
<div class="eyebrow" style="left:171px;top:958px">Herzlich willkommen in ihrem</div>
<h1 class="heading heading-xl" style="left:100px;top:973px">5 Sterne Strandhaus</h1>
<p class="body-copy" style="left:100px;top:1034px;width:480px">Dieses exklusive, 2017 erbaute Strandhaus mit ca. 145 m² Wohnfläche und einem Grundstück von ca. 700 m² befindet sich ca. 5 Gehminuten vom Strand entfernt.</p>
<div class="btn-gold" style="left:100px;top:1132px;width:166px;height:41px;font-size:15px">Mehr Erfahren</div>

<div class="cream-bg" style="left:836px;top:947px;width:249px;height:78px;background:#efebdd"></div>
<div class="cream-bg" style="left:683px;top:1144px;width:153px;height:18px;background:#efebdd"></div>
<div class="photo" style="left:802px;top:878px;width:271px;height:69px;background:linear-gradient(90deg,#4d5a44,#8a7f8a,#6b6250)" role="img" aria-label="Gartenhaus mit Lavendel"></div>
<div class="photo" style="left:655px;top:949px;width:294px;height:195px;background:linear-gradient(160deg,#4a78b8 0%,#8fb0d8 30%,#d9d8d0 55%,#6f7f4a 100%)" role="img" aria-label="Reetdachhaus unter blauem Himmel"></div>
<div class="photo" style="left:949px;top:947px;width:124px;height:78px;background:linear-gradient(135deg,#7c7a5e,#3aa8a8 60%,#8c6d4c)" role="img" aria-label="Türkise Windlichter auf dem Terrassentisch"></div>
<div class="photo" style="left:836px;top:1025px;width:263px;height:177px;background:linear-gradient(160deg,#7fa0c8 0%,#e8e8e6 40%,#b9bcbc 75%,#8d9796 100%)" role="img" aria-label="Whirlpool auf der Terrasse"></div>

<!-- detail section -->
<div class="cream-bg" style="left:0;top:1345px;width:1134px;height:739px"></div>
<div class="photo" style="left:0;top:1375px;width:571px;height:398px;background:linear-gradient(120deg,#3e4434 0%,#6f6a52 35%,#a89b82 60%,#8c7a60 100%)" role="img" aria-label="Rotweingläser und Lavendel auf dem Terrassentisch"></div>
<p class="body-copy" style="left:613px;top:1458px;width:480px">Dieses exklusive, 2017 erbaute Strandhaus mit ca. 145 m² Wohnfläche und einem Grundstück von ca. 700 m² befindet sich ca. 5 Gehminuten vom Strand entfernt.</p>
<div class="paper-box" style="left:812px;top:1616px;width:388px;height:468px;background:var(--white)"></div>
<div class="paper-box" style="left:68px;top:1773px;width:745px;height:311px;background:var(--white)"></div>
<p class="body-copy" style="left:95px;top:1878px;width:480px">Das Haus verfügt über beheizbarer Aussenwhirlpool (ganzjährig nutzbar), Safe, Internet – WLAN, Sauna mit Infrarot, 2 Terrassen, HWR mit Waschmaschine und Trockner, Bollerwagen, Parkplatz.</p>
<div class="photo" style="left:629px;top:1648px;width:571px;height:397px;background:linear-gradient(110deg,#d8d6d0 0%,#f2f1ec 30%,#c9a46a 55%,#4d7a5a 75%,#2fa6a0 100%)" role="img" aria-label="Bad und Wohnraum mit Liegestühlen vor der Glasfront"></div>

<!-- banner -->
<div class="photo" style="left:0;top:2084px;width:1200px;height:384px;background:linear-gradient(180deg,#1f2e5a 0%,#2a3a68 45%,#7b6f58 75%,#c8b896 100%)" role="img" aria-label="Gräser im Abendlicht vor dunkelblauem Himmel"></div>
<div class="cream-bg" style="left:0;top:2468px;width:1200px;height:103px"></div>
<p class="body-copy" style="left:337px;top:2496px;width:620px">Egal ob Sommer oder Winter, in unserem Haus wird ihr Urlaub zum Erlebnis. Am Sommer gehen Sie zum Stand und im Winter genießen Sie ihre eigene Sauna und Whirlpool.</p>

<!-- faq -->
<section aria-label="Häufige Fragen">
  <div class="eyebrow" style="left:262px;top:2655px">Häufige Fragen</div>
  <h2 class="heading heading-l" style="left:192px;top:2668px">Schnell beantwortet</h2>
  <div class="q" style="left:194px;top:2758px">WANN IST CHECK-IN? &nbsp;⌄</div>
  <p class="body-copy" style="left:194px;top:2786px;width:560px;font-size:12.5px;line-height:21px">Lorem ipsum dolor sit amet, consetetur sadipscing elitr, sed diam nonumy eirmod tempor invidunt ut labore et dolore magna aliquyam erat, sed diam voluptua. At vero eos et accusam et justo duo dolores et ea rebum. Stet clita kasd gubergren.</p>
  <div class="divider" style="left:194px;top:2882px;width:552px"></div>
  <div class="q" style="left:194px;top:2908px">IST EINE LANGZEIT MIETE MÖGLICH? &nbsp;›</div>
  <div class="divider" style="left:194px;top:2945px;width:552px"></div>
  <div class="q" style="left:194px;top:2973px">GIBT ES CORONA AUFLAGEN? ›</div>
  <div class="q" style="left:859px;top:2758px">SIE HABEN EINE FRAGE?</div>
  <p class="body-copy" style="left:859px;top:2784px;width:150px;font-size:12.5px;line-height:22.5px">Sollten Sie noch offene Fragen haben, so kontaktieren Sie uns einfach.</p>
  <div class="btn-gold" style="left:859px;top:2893px;width:113px;height:31px;font-size:13.5px">Frage stellen</div>
</section>

<!-- location -->
<div class="photo" style="left:0;top:3076px;width:1200px;height:370px;background:linear-gradient(100deg,#bdbdbd 0%,#a8a8a8 35%,#c6c6c6 60%,#dcdcdc 80%,#c2c2c2 100%)" role="img" aria-label="Karte der Umgebung von Holmstede"></div>
<svg class="abs" style="left:880px;top:3236px" width="26" height="36" viewBox="0 0 26 36"><path d="M13 1a11 11 0 00-11 11c0 8 11 23 11 23s11-15 11-23A11 11 0 0013 1z" fill="#111"/><circle cx="13" cy="12" r="4" fill="#fff"/></svg>

<footer class="site-footer">
  <div class="footer-brand">
    <div class="brand-name">KIEFERNVILLA<br>HOLMSTEDE</div>
  </div>
  <nav class="footer-nav"><span>Das 5* Strandhaus</span><span>Verfügbarkeit</span><span>Die Räumlichkeiten</span><span>Lage</span><span>Kontakt</span></nav>
  <div class="footer-rule"></div>
  <div class="footer-legal"><span>Impressum</span><span>Datenschutz</span></div>
  <p class="footer-about">Exklusives schilfrohrgedecktes, 2017 erbautes<br>Strandhaus in der 5-Sterne-Haus-Anlage<br>"NORELA Küstenland" in Holmstede.</p>
</footer>

</body>
</html>
```